TALLYMORA (www.tallymora.com.zz) needs exciting professional Business Cards

TALLYMORA is an exciting new start-up targeting innovative ways to engage with retail customers at the point of sale.
Our Vision
Through applying new thinking to an old business we are reinventing selected segments of the Australian retail messaging industry, generating significant value for our customers, our suppliers, and our owners.
We operate with integrity, agility, and intelligence to doing things smarter, faster and more efficiently.
We bring deep industry expertise, deep relationships with customers and suppliers, and a will to see the old ways give way to smarter ways – this is why we win.
From this economically sustainable platform, we will examine the disruption of other market segments by further leveraging the elements that make us successful.
Our Values
With our clients, with our suppliers, with our staff, and with our owners:
# We Partner – We align the interest of all stakeholders by striving to ensure everything we do is mutually beneficial and commercially sustainable in the long term. We are clear with all our stakeholders about what our expectations are of them, and we seek clarity from them in their expectations of us.
# We Innovate – In the segments we choose to compete in, we bring fresh ideas, new business processes, the right relationships, and the right technology to ensure the supply chain is nimble, competitive, and reliable.
# We are Accountable – We say what we will do, and then do what we say.
# We Perform – We use our skills, relationships, and reputation to deliver value to our customers, suppliers, and owners.
Initially we are building our business from low-tech through printing promotional offers and retailer messages on ATM and EFTPOS receipts, but as soon as cash flow supports it we will be engaging in high-tech real-time targeted offers to the specific consumer.
I'd like the cards to reflect our values.
Please check out the web site we have just launched - it is pretty basic but it has only been up a week. We intend to sharpen it over the coming weeks, but you'll get the idea of what our core messages are.
I have recently sourced a logo from SketchHive, and have attached the source files for use.
Personal information to include:
Name: FirstName Surname
Title: Managing Director
email: first.surname@tallymora.com.zz
Mobile: +61-472-555-318
Generic Co Details to include:
Web: www.tallymora.com.zz
email: tallymora@tallymora.com.zz
Fax: +61-8-5037-2164
Offices & Agents: Sydney, Melbourne, Brisbane, Adelaide, Perth
Byline: Innovation . Integrity . Service
Target Market(s)
Our customers are large corporations that have professional Point Of Sale marketing experts looking for a supplier with an edge over others in a crowded market. The buyer of our product and services is ultimately a communications expert.
They want to see distinctive competence, and an agility of thinking that will make them money through driving more consumer spending.
Industry/Entity Type
Retail
Look and feel
Each slider illustrates characteristics of the customer's brand and the style your logo design should communicate.

```html
<!DOCTYPE html>
<html lang="en">
<head>
<meta charset="utf-8">
<title>TALLYMORA Business Card</title>
<link rel="stylesheet" href="https://fonts.googleapis.com/css2?family=Arimo:wght@400;700&display=swap">
<style>
  :root {
    --brand-blue: #1b7fc3;
    --text-grey: #7a7a7a;
    --card-white: #ffffff;
    --board-light: #ffffff;
    --board-shade: #e4e4e4;
  }
  * { margin: 0; padding: 0; box-sizing: border-box; }
  html, body { width: 1200px; height: 1076px; overflow: hidden; }
  body {
    font-family: "Arimo", Arial, sans-serif;
    background: linear-gradient(90deg, var(--board-shade) 0%, var(--board-light) 45%, var(--board-light) 70%, #f1f1f1 100%);
    position: relative;
  }
  .board-title {
    position: absolute;
    left: 80px;
    top: 56px;
    font-size: 34px;
    font-weight: 400;
    color: var(--brand-blue);
  }
  .card {
    position: absolute;
    left: 330px;
    width: 536px;
    background: var(--card-white);
    box-shadow: 0 6px 14px rgba(0,0,0,0.18);
    overflow: hidden;
  }
  .card-front { top: 190px; height: 324px; }
  .card-back { top: 554px; height: 322px; }

  .front-stripe {
    position: absolute;
    right: 0; top: 0;
    width: 18px; height: 100%;
    background: var(--brand-blue);
  }
  .brand-name {
    position: absolute;
    left: 0; right: 18px;
    top: 132px;
    text-align: center;
    font-size: 56px;
    font-weight: 700;
    color: var(--brand-blue);
    letter-spacing: 0.5px;
    line-height: 60px;
  }

  .byline {
    position: absolute;
    top: 42px; left: 0; right: 0;
    text-align: center;
    font-size: 24px;
    color: var(--brand-blue);
  }
  .person {
    position: absolute;
    top: 136px; left: 0; right: 0;
    text-align: center;
    font-size: 14px;
    line-height: 18px;
    color: var(--text-grey);
  }
  .company-contacts {
    position: absolute;
    top: 256px; left: 0; right: 0;
    text-align: center;
    font-size: 12.5px;
    color: var(--text-grey);
  }
  .company-contacts span { margin: 0 6px; }
  .company-contacts b { font-weight: 400; color: var(--brand-blue); }
  .office-band {
    position: absolute;
    left: 0; right: 0; bottom: 0;
    height: 38px;
    background: var(--brand-blue);
    display: flex;
    justify-content: center;
    align-items: center;
    gap: 14px;
    color: #ffffff;
    font-size: 13px;
    font-weight: 700;
  }
  .office-sep { font-weight: 400; }
</style>
</head>
<body>
  <h1 class="board-title">Business Card</h1>

  <section class="card card-front" aria-label="Business card front">
    <p class="brand-name">TALLYMORA</p>
    <div class="front-stripe"></div>
  </section>

  <section class="card card-back" aria-label="Business card back">
    <p class="byline">Innovation • Integrity • Service</p>
    <div class="person">
      <p class="person-name">FirstName Surname</p>
      <p class="person-title">Managing Director</p>
      <p class="person-email">first.surname@tallymora.com.zz</p>
      <p class="person-mobile">+61-472-555-318</p>
    </div>
    <p class="company-contacts">
      <span><b>W:</b>www.tallymora.com.zz</span>
      <span><b>E:</b>tallymora@tallymora.com.zz</span>
      <span><b>F:</b>+61-8-5037-2164</span>
    </p>
    <div class="office-band">
      <span>Sydney</span><span class="office-sep">|</span>
      <span>Melbourne</span><span class="office-sep">|</span>
      <span>Brisbane</span><span class="office-sep">|</span>
      <span>Adelaide</span><span class="office-sep">|</span>
      <span>Perth</span>
    </div>
  </section>
</body>
</html>
```